Healthcare IT firm needs classy and unique business care design

We need a business card design that incorporates our new logo design (attached) Prefer a purple based designed. I would really love to see something utilizing the "3D" version of the logo (purple on the reflective wall). I want something a little more than my logo printed along with a person's detailed contact information.
Contact Information for Business Card
Want something polished, professional, and a little unique in the design.
Colors
6b449b
Requirements
Must have
- Please use similar font as the logo design
Nice to have
- Would like to see the 3d version of my logo incorporated into the design.

```html
<!DOCTYPE html>
<html lang="en">
<head>
<meta charset="utf-8">
<title>Nearline Health Systems – Business Card</title>
<link rel="stylesheet" href="https://fonts.googleapis.com/css2?family=Lato:wght@400;700;900&display=swap">
<style>
  :root {
    --backdrop: #2b2b2b;
    --card-top: #1a1a1a;
    --card-bottom: #0b0b0b;
    --brand-purple: #6b449b;
    --accent-purple: #7a4fb3;
    --text-light: #d4d4d4;
    --text-muted: #a9a9a9;
    --divider: #5a5a5a;
  }
  * { box-sizing: border-box; margin: 0; padding: 0; }
  html, body {
    width: 1200px;
    height: 900px;
    overflow: hidden;
    background: var(--backdrop);
    font-family: "Lato", Arial, sans-serif;
  }
  .canvas {
    position: relative;
    width: 1200px;
    height: 900px;
    display: flex;
    flex-direction: column;
    align-items: center;
    justify-content: center;
    gap: 40px;
  }
  .card {
    position: relative;
    width: 560px;
    height: 320px;
    background: linear-gradient(160deg, var(--card-top), var(--card-bottom));
    overflow: hidden;
  }
  .card__band {
    position: absolute;
    left: 0;
    right: 0;
    bottom: 0;
    height: 10px;
    background: var(--accent-purple);
  }

  /* Front */
  .card--front {
    display: flex;
    align-items: center;
    justify-content: center;
  }
  .brand-name {
    color: var(--brand-purple);
    font-weight: 900;
    font-size: 38px;
    letter-spacing: -0.5px;
    text-align: center;
    line-height: 1.05;
    margin-bottom: 16px;
  }

  /* Back */
  .card--back {
    padding: 92px 0 0 70px;
  }
  .card__details {
    display: flex;
    align-items: stretch;
  }
  .person {
    width: 170px;
    padding-top: 6px;
  }
  .person__name {
    color: var(--accent-purple);
    font-weight: 700;
    font-size: 21px;
    text-transform: uppercase;
    letter-spacing: 0.2px;
    white-space: nowrap;
  }
  .person__title {
    color: var(--text-muted);
    font-size: 15px;
    margin-top: 2px;
  }
  .card__divider {
    width: 1px;
    background: var(--divider);
    margin: 0 22px 0 10px;
  }
  .contact-list {
    list-style: none;
    display: flex;
    flex-direction: column;
    gap: 4px;
  }
  .contact-list__item {
    display: flex;
    align-items: center;
    gap: 10px;
    color: var(--text-light);
    font-size: 15.5px;
    letter-spacing: 0.2px;
    white-space: nowrap;
  }
  .contact-list__icon {
    width: 13px;
    height: 13px;
    flex: none;
    fill: var(--text-muted);
  }
  .card__address {
    color: var(--text-light);
    font-size: 15.5px;
    letter-spacing: 0.2px;
    margin-top: 28px;
    white-space: nowrap;
  }
</style>
</head>
<body>
<main class="canvas">
  <section class="card card--front" aria-label="Card front">
    <h1 class="brand-name">Nearline<br>Health Systems</h1>
    <div class="card__band"></div>
  </section>

  <section class="card card--back" aria-label="Card back">
    <div class="card__details">
      <div class="person">
        <p class="person__name">Daniel Reed</p>
        <p class="person__title">Managing Director</p>
      </div>
      <div class="card__divider"></div>
      <ul class="contact-list">
        <li class="contact-list__item">
          <svg class="contact-list__icon" viewBox="0 0 16 16" aria-hidden="true"><path d="M2 5c0-2 2-3 6-3s6 1 6 3v1h-3l-1-2H6L5 6H2z M4 7h8l2 6H2z"/></svg>
          020-555 018 274
        </li>
        <li class="contact-list__item">
          <svg class="contact-list__icon" viewBox="0 0 16 16" aria-hidden="true"><path d="M4 1h8v14H4z M5.5 3v9h5V3z M7 13h2v1H7z" fill-rule="evenodd"/></svg>
          020-555 018 391
        </li>
        <li class="contact-list__item">
          <svg class="contact-list__icon" viewBox="0 0 16 16" aria-hidden="true"><path d="M1 3h14v10H1z M2 4l6 5 6-5" fill-rule="evenodd"/></svg>
          hello@nearline.com
        </li>
        <li class="contact-list__item">
          <svg class="contact-list__icon" viewBox="0 0 16 16" aria-hidden="true"><circle cx="8" cy="8" r="7"/></svg>
          www.nearlinehealth.com
        </li>
      </ul>
    </div>
    <p class="card__address">48 Harbour Lane, Millbrook Park, Eastvale, 20714.</p>
    <div class="card__band"></div>
  </section>
</main>
</body>
</html>
```